Bright Path Attorneys Billboard Design for Personal Injury Law Firm

Need a billboard design that we can use for different versions. 1400px X 400px jpeg or png
I have attached the logo and the attorney for the billboard. Attorney Marla Benning
Here is a link to our current website brightpathlegalgroup.example

HEADLINE: HIT BY A TRUCK?
SUBHEAD: NO FEE. BIG FIGHT.
877-GRANTLY

HEADLINE: ACCIDENT?
SUBHEAD: NO FEE, UNLESS WE WIN!
877-GRANTLY

HEADLINE: BIG TRUCK. BIG CASE.
SUBHEAD: YOU PAY $0 UPFRONT
877-GRANTLY

Target Market(s)

People in Car Accident

Industry/Entity Type

Personal Injury Attorneys

```html
<!DOCTYPE html>
<html lang="en">
<head>
<meta charset="utf-8">
<title>Bright Path Attorneys – Billboard Set</title>
<link href="https://fonts.googleapis.com/css2?family=Oswald:wght@600;700&family=Montserrat:wght@500;600&display=swap" rel="stylesheet">
<style>
  :root {
    --page: #ffffff;
    --board: #000000;
    --white: #ffffff;
    --gold: #f9c510;
    --rule: #e7b40d;
  }
  * { margin: 0; padding: 0; box-sizing: border-box; }
  html, body { width: 1200px; height: 1138px; overflow: hidden; background: var(--page); }
  .sheet { position: relative; width: 1200px; height: 1138px; }

  .billboard {
    position: absolute; left: 51px; width: 1101px; height: 315px;
    background: var(--board); overflow: hidden;
    font-family: "Oswald", "Arial Narrow", sans-serif; font-weight: 700;
  }
  .billboard--truck { top: 66px; }
  .billboard--accident { top: 426px; }
  .billboard--bigcase { top: 775px; }

  .photo { position: absolute; top: 0; right: 0; height: 100%; }
  .photo::after {
    content: ""; position: absolute; inset: 0;
    background: linear-gradient(90deg, var(--board) 0%, rgba(0,0,0,.6) 14%, rgba(0,0,0,0) 32%);
  }
  .billboard--truck .photo {
    width: 420px;
    background: radial-gradient(ellipse at 68% 55%, #a9a49b 0%, #7c7a73 30%, transparent 60%),
                linear-gradient(160deg, #4f5a3c 0%, #3d4530 35%, #5c5e58 70%, #3a3b3a 100%);
  }
  .billboard--accident .photo {
    width: 470px;
    background: radial-gradient(ellipse at 70% 50%, #8a8b90 0%, #5e5c66 35%, transparent 65%),
                linear-gradient(170deg, #3c3b36 0%, #4a4652 45%, #2a2630 100%);
  }
  .billboard--bigcase .photo {
    width: 505px;
    background: radial-gradient(ellipse at 66% 62%, #3c3f45 0%, #2a2c31 30%, transparent 55%),
                linear-gradient(180deg, #3b8c9a 0%, #7eaab0 28%, #d9a065 46%, #5d5850 58%, #3a3a3c 100%);
  }

  .line { position: absolute; white-space: nowrap; line-height: 1; }
  .headline { color: var(--white); font-size: 84px; letter-spacing: 1px; }
  .subhead { color: var(--gold); font-size: 51px; letter-spacing: 1.5px; }
  .cta { color: var(--gold); font-size: 60px; letter-spacing: 1px; }
  .cta--small { font-size: 44px; letter-spacing: .5px; }

  .rule {
    position: absolute; left: 99px; width: 506px; height: 3px;
    background: linear-gradient(90deg, transparent 0%, var(--rule) 8%, var(--rule) 92%, transparent 100%);
  }

  .firm {
    position: absolute; left: 748px; top: 255px;
    display: flex; align-items: center; gap: 12px;
    color: var(--white); font-family: "Montserrat", sans-serif; font-weight: 600;
    font-size: 22px; letter-spacing: 1px; text-transform: uppercase; white-space: nowrap;
  }
  .firm__dot { width: 14px; height: 14px; border-radius: 50%; background: var(--white); }
</style>
</head>
<body>
<main class="sheet">

  <section class="billboard billboard--truck">
    <div class="photo" role="img" aria-label="Silver semi truck driving on a tree-lined road"></div>
    <h2 class="line headline" style="left:34px; top:32px;">HIT BY A TRUCK?</h2>
    <div class="rule" style="top:123px;"></div>
    <p class="line subhead" style="left:125px; top:135px;">NO FEE. BIG FIGHT</p>
    <div class="rule" style="top:202px;"></div>
    <p class="line cta" style="left:65px; top:210px;">CTA: 877-GRANTLY</p>
    <div class="firm"><span class="firm__dot"></span>Bright Path Attorneys</div>
  </section>

  <section class="billboard billboard--accident">
    <div class="photo" role="img" aria-label="Two cars after a collision on a wooded roadside"></div>
    <h2 class="line headline" style="left:31px; top:30px;">ACCIDENT?</h2>
    <div class="rule" style="top:128px;"></div>
    <p class="line subhead" style="left:30px; top:141px;">NO FEE, UNLESS WE WIN!</p>
    <div class="rule" style="top:210px;"></div>
    <p class="line cta cta--small" style="left:30px; top:226px;">CTA (DOMINANT): 877-GRANTLY</p>
    <div class="firm"><span class="firm__dot"></span>Bright Path Attorneys</div>
  </section>

  <section class="billboard billboard--bigcase">
    <div class="photo" role="img" aria-label="Dark semi truck on an open highway at sunset"></div>
    <h2 class="line headline" style="left:48px; top:27px;">BIG TRUCK. BIG CASE.</h2>
    <div class="rule" style="top:128px;"></div>
    <p class="line subhead" style="left:87px; top:141px;">YOU PAY $0 UPFRONT</p>
    <div class="rule" style="top:210px;"></div>
    <p class="line cta" style="left:65px; top:218px;">CTA: 877-GRANTLY</p>
    <div class="firm"><span class="firm__dot"></span>Bright Path Attorneys</div>
  </section>

</main>
</body>
</html>
```